A new type of air filter for interior of vehicles

HI
I have included a file to show the basics of what i want and all the information that should be needed ,i now need this to be "designed" and to be created for a information flyer first and as things progress web pages etc etc look forward to the designs

Industry/Entity Type

Interior

Contact Information for Business Card

probably the same "theme type" as the brochure which will carry through to Business card and on to online marketing in the future

Font styles to use
Serif
Sans Serif

```html
<!DOCTYPE html>
<html lang="en">
<head>
<meta charset="utf-8">
<title>ClearCabin Filters Co – Flyer and Business Cards</title>
<link href="https://fonts.googleapis.com/css2?family=Open+Sans:wght@400;600;700&family=PT+Sans:wght@400;700&family=Oswald:wght@600&display=swap" rel="stylesheet">
<style>
  :root{
    --bg:#ecebe8;
    --brand-red:#c01f2f;
    --band-grey:#55565a;
    --sky-top:#2f6fc4;
    --sky-mid:#7fb2e6;
    --sky-low:#d9ebfa;
    --ink:#3c3c3c;
    --heading-red:#c0202e;
    --card-blue:#cfe6fa;
    --card-blue-light:#f1f8fe;
    --link-blue:#1f6fbf;
    --label:#222;
    --white:#ffffff;
  }
  *{box-sizing:border-box;margin:0;padding:0}
  html,body{width:1200px;height:1060px;overflow:hidden}
  body{background:var(--bg);position:relative;font-family:"Open Sans",Arial,sans-serif;color:var(--ink)}

  /* ---------- flyer ---------- */
  .flyer{position:absolute;left:119px;top:64px;width:655px;height:927px;background:var(--white);overflow:hidden;box-shadow:0 2px 10px rgba(0,0,0,.25)}
  .flyer-hero{position:absolute;left:0;top:0;width:655px;height:400px;
    background:radial-gradient(ellipse 45% 40% at 55% 45%, rgba(255,255,255,.55), rgba(255,255,255,0) 70%),
               linear-gradient(180deg,var(--sky-top) 0%,var(--sky-mid) 45%,var(--sky-low) 100%)}
  .flyer-shapes{position:absolute;left:0;top:0}
  .flyer-title{position:absolute;left:0;width:655px;top:38px;text-align:center;font-family:"PT Sans",Arial,sans-serif;font-weight:700;font-size:45px;color:var(--white);text-shadow:0 3px 5px rgba(0,0,0,.55);letter-spacing:.5px}
  .flyer-web{position:absolute;left:52px;top:296px;width:600px;font-family:"PT Sans",Arial,sans-serif;font-weight:700;font-size:24px;letter-spacing:2.6px;color:var(--white);transform:rotate(3.5deg);transform-origin:left center;white-space:nowrap}

  .info{position:absolute;left:33px;width:414px}
  .info h2{font-family:"PT Sans",Arial,sans-serif;font-weight:700;font-size:18px;line-height:22px;color:var(--heading-red);margin-bottom:6px}
  .info p{font-family:"PT Sans",Arial,sans-serif;font-size:9.6px;line-height:11.4px;text-align:justify}
  .info-1{top:380px}.info-2{top:476px}.info-3{top:584px}.info-4{top:722px}

  .info-photo{position:absolute;left:481px;width:146px;border:1px solid #b9b9b9;border-radius:9px;box-shadow:0 2px 4px rgba(0,0,0,.2)}
  .photo-vent{top:379px;height:90px;background:linear-gradient(135deg,#e8e8e8,#8d8f93 60%,#4b4d52)}
  .photo-exhaust{top:479px;height:103px;background:linear-gradient(160deg,#b3cbe6,#d9dde2 45%,#5e6166 80%)}
  .photo-media{top:596px;height:104px;background:linear-gradient(90deg,#f3f3f3 30%,#2b2b2e 40%,#3a3a3d 70%,#f3f3f3 78%)}
  .photo-frame{top:715px;height:110px;background:linear-gradient(90deg,#f3f3f3 22%,#28282b 30%,#3b2325 60%,#f3f3f3 76%)}

  .flyer-seal{position:absolute;left:515px;top:808px;width:78px;height:78px;border-radius:50%;background:radial-gradient(circle at 40% 35%,#8fc3f0,#1f5fb0);border:5px solid var(--brand-red);box-shadow:0 0 0 2px var(--white)}
  .flyer-address{position:absolute;left:33px;top:874px;font-size:11px;color:var(--white)}
  .flyer-contact{position:absolute;left:33px;top:894px;font-size:14px;color:var(--white);white-space:nowrap}
  .flyer-contact b{font-weight:700}
  .flyer-contact .call{margin-left:20px}
  .flyer-contact .call b{font-size:17px}

  /* ---------- option labels ---------- */
  .option-label{position:absolute;font-family:"Oswald",Arial,sans-serif;font-weight:600;font-size:21px;color:var(--label)}

  /* ---------- business cards ---------- */
  .card{position:absolute;overflow:hidden;background:linear-gradient(135deg,var(--card-blue-light),var(--card-blue));box-shadow:0 2px 6px rgba(0,0,0,.25)}
  .card-art{position:absolute;background:radial-gradient(circle at 50% 35%,#dff0ff 0%,#6fa8e0 38%,#e9c7a8 62%,rgba(233,199,168,0) 78%)}

  .card-one{left:829px;top:145px;width:277px;height:157px}
  .card-one .card-art{left:12px;top:10px;width:115px;height:140px}
  .card-one .contact-list{position:absolute;right:10px;top:14px;text-align:right;font-size:7px;line-height:11px;color:#333}
  .contact-list .dot{display:inline-block;width:5px;height:5px;border:1px solid #555;border-radius:50%;margin-left:4px;vertical-align:middle}
  .card-one .contact-list .site{font-weight:700}
  .card-one .person{position:absolute;right:12px;top:84px;font-size:9px;font-weight:700;color:#333}
  .person .role{font-weight:400;font-size:7px;letter-spacing:.3px;color:#555}
  .card-one .name-band{position:absolute;left:98px;top:124px;width:179px;height:19px;background:var(--brand-red);border-radius:10px 0 0 10px;color:var(--white);font-family:"PT Sans",Arial,sans-serif;font-weight:700;font-size:11.5px;line-height:19px;text-align:right;padding-right:8px}

  .card-two{left:829px;top:383px;width:277px;height:157px}
  .card-two .person{position:absolute;left:0;width:100%;top:9px;text-align:center;font-size:8px;font-weight:700;color:#333}
  .card-two .card-art{left:88px;top:24px;width:100px;height:70px}
  .card-two .brand-name{position:absolute;left:0;width:100%;top:92px;text-align:center;font-family:"PT Sans",Arial,sans-serif;font-weight:700;font-size:12.5px;color:var(--brand-red)}
  .card-two .band-left{position:absolute;left:0;top:109px;width:150px;height:12px;background:var(--link-blue);color:var(--white);font-size:6.3px;line-height:12px;padding-left:12px}
  .card-two .band-right{position:absolute;left:144px;top:109px;width:133px;height:12px;background:var(--brand-red);color:var(--white);font-size:6.3px;line-height:12px;padding-left:12px;font-weight:600;clip-path:polygon(8px 0,100% 0,100% 100%,0 100%)}
  .card-two .contact-line{position:absolute;left:0;width:100%;top:131px;text-align:center;font-size:6.5px;color:#333}
  .contact-line .key{color:var(--link-blue)}

  .card-three{left:888px;top:618px;width:159px;height:276px;background:linear-gradient(180deg,var(--card-blue-light),var(--card-blue))}
  .card-three .card-photo{position:absolute;left:0;top:0;width:159px;height:112px;background:radial-gradient(ellipse 40% 40% at 55% 45%,rgba(255,255,255,.5),rgba(255,255,255,0) 70%),linear-gradient(180deg,var(--sky-top),var(--sky-mid) 55%,var(--sky-low))}
  .card-three svg{position:absolute;left:0;top:0}
  .card-three .brand-name{position:absolute;left:0;width:100%;top:138px;text-align:center;font-family:"PT Sans",Arial,sans-serif;font-weight:700;font-size:13px;line-height:15px;color:var(--link-blue)}
  .card-three .person{position:absolute;left:0;width:100%;top:186px;text-align:center;font-size:8px;font-weight:700;color:#333}
  .card-three .contact-stack{position:absolute;left:0;width:100%;top:212px;text-align:center;font-size:6.5px;line-height:10.5px;color:#333}
  .card-three .contact-stack .key{color:var(--link-blue)}
  .card-three .contact-stack .site{display:block;margin-top:5px;font-weight:700}
</style>
</head>
<body>

  <!-- Flyer -->
  <section class="flyer">
    <div class="flyer-hero" role="img" aria-label="Blue sky with clouds and two open hands holding a clear bubble with a car outline inside"></div>
    <svg class="flyer-shapes" width="655" height="927" viewBox="0 0 655 927" aria-hidden="true">
      <polygon points="0,267 655,307 655,357 0,302" fill="var(--brand-red)"/>
      <polygon points="0,302 655,357 655,370 0,312" fill="var(--band-grey)"/>
      <polygon points="0,312 655,370 655,927 0,927" fill="var(--white)"/>
      <polygon points="0,830 655,872 655,927 0,927" fill="var(--band-grey)"/>
      <polygon points="0,838 655,882 655,927 0,927" fill="var(--brand-red)"/>
    </svg>
    <h1 class="flyer-title">ClearCabin Filters Co</h1>
    <div class="flyer-web">www.ClearCabinFilters.com.au</div>

    <article class="info info-1">
      <h2>What is a Cabin Air Filter ?</h2>
      <p>Cabin air filters with dual layer carbon activated filter media, are designed to remove nearly 100% of airborn particles, like pollen,road dust,soot and other microscopic particles.The activated carbon also helps to remove over 80% of noxious fumes emitting from your vehicles air vents.</p>
    </article>
    <article class="info info-2">
      <h2>Why is a Cabin Air Filter important ?</h2>
      <p>Surrounding traffic creates poisonous gases and heavy metal pollutants that are directed straight into your vehicles interior.Apart the obvious health concerns unfiltered air can lead to allergies, asthma and other respiratory problems.With over 4 million Australians suffering from allergies, our activated carbon cabin filter are an essential part of your vehicles ventilation system.</p>
    </article>
    <article class="info info-3">
      <h2>How do Cabin Air Filters work ?</h2>
      <p>Our Cabin Air Filters work by filtering the outside air entering your vehicle.ClearCabin Filters Co's unique design has a first layer of sponge like material, coated in a layer of activated carbon(each gram has the same surface area as a football field) this layer traps larger particles and helps absorb odours while maintaining the maximum surface filtering area .The second layer of fine spun micro fibre also coated in activated carbon helps trap dangerous smaller microscopic particles and provides an extra layer of absorption while still maintaining maximum air flow</p>
    </article>
    <article class="info info-4">
      <h2>Why is ClearCabin Filters Co Different ?</h2>
      <p>Our Cabin Filters are a complete new Australian design. By greatly increasing the surface area in contact with incoming air, over conventional type "pleated filters" we are able to maintain high air flow while greatly increasing filtering capacity, with the added benefit of activated carbon coating in contact with all areas of air flow. All our filter support bases are low allergy, cast acylic, laser cut to suit individual vehicles,and our activated carbon is sourced from coconut shells Our 2 stages of filter media is of the highest quality available.</p>
    </article>

    <div class="info-photo photo-vent" role="img" aria-label="Car dashboard air vent with air flowing out"></div>
    <div class="info-photo photo-exhaust" role="img" aria-label="Vehicle exhaust pipe releasing smoke"></div>
    <div class="info-photo photo-media" role="img" aria-label="Close-up of layered carbon filter media"></div>
    <div class="info-photo photo-frame" role="img" aria-label="Cabin filter with red cut acrylic support frame"></div>

    <div class="flyer-seal" role="img" aria-label="Round seal badge"></div>
    <p class="flyer-address">PO Box 12 Harbour Point Qld 4300</p>
    <p class="flyer-contact"><b>Email :</b> hello@clearcabinfilters.com.au <span class="call">Call : <b>0400 555 019</b></span></p>
  </section>

  <!-- Option labels -->
  <div class="option-label" style="left:928px;top:100px">Option 1</div>
  <div class="option-label" style="left:935px;top:345px">Option 2</div>
  <div class="option-label" style="left:938px;top:576px">Option 3</div>

  <!-- Card option 1 -->
  <section class="card card-one">
    <div class="card-art" role="img" aria-label="Two open hands holding a clear bubble with a car outline"></div>
    <div class="contact-list">
      <div>0400 555 019<span class="dot"></span></div>
      <div>hello@clearcabinfilters.com.au<span class="dot"></span></div>
      <div>PO Box 12 Harbour Point Qld 4300<span class="dot"></span></div>
      <div class="site">ClearCabinFilters.com.au<span class="dot"></span></div>
    </div>
    <div class="person">Warren <span class="role">| DIRECTOR</span></div>
    <div class="name-band">ClearCabin Filters Co</div>
  </section>

  <!-- Card option 2 -->
  <section class="card card-two">
    <div class="person">Warren, <span class="role">DIRECTOR</span></div>
    <div class="card-art" role="img" aria-label="Two open hands holding a clear bubble with a car outline"></div>
    <div class="brand-name">ClearCabin Filters Co</div>
    <div class="band-left">PO Box 12 Harbour Point Qld 4300</div>
    <div class="band-right">ClearCabinFilters.com.au</div>
    <div class="contact-line"><span class="key">Phone :</span> 0400 555 019 &nbsp;|&nbsp; <span class="key">Email :</span> hello@clearcabinfilters.com.au</div>
  </section>

  <!-- Card option 3 -->
  <section class="card card-three">
    <div class="card-photo" role="img" aria-label="Blue sky with bubbles and two open hands holding a bubble with a car outline"></div>
    <svg width="159" height="276" viewBox="0 0 159 276" aria-hidden="true">
      <polygon points="0,84 159,112 159,120 0,92" fill="var(--brand-red)"/>
      <polygon points="0,92 159,120 159,124 0,96" fill="var(--band-grey)"/>
      <polygon points="0,96 159,124 159,276 0,276" fill="var(--card-blue-light)"/>
    </svg>
    <div class="brand-name">ClearCabin Filters<br>Co</div>
    <div class="person">Warren, <span class="role">DIRECTOR</span></div>
    <div class="contact-stack">
      <div><span class="key">Phone :</span> 0400 555 019</div>
      <div><span class="key">Email :</span> hello@clearcabinfilters.com.au</div>
      <div>PO Box 12 Harbour Point Qld 4300</div>
      <span class="site">www.ClearCabinFilters.com.au</span>
    </div>
  </section>

</body>
</html>
```